Web Design Project

I want customers to be able to book appointments to get their makeup done and make a deposit and also have a gallery where i put my portfolio images, i want it to be very simple yet elegant.

Target Market(s)

Women ranging from 18-40 that want to get their makeup done

Industry/Entity Type

Makeup

Font styles to use
Sans Serif
Decorative

Requirements
Nice to have
• easy scheduling option and option to pay service in full on website.

```html
<!DOCTYPE html>
<html lang="en">
<head>
<meta charset="utf-8">
<title>Glowhouse – Homepage and Booking Step 1</title>
<link rel="stylesheet" href="https://fonts.googleapis.com/css2?family=Raleway:wght@400;500;600;700;800&family=Old+Standard+TT:ital,wght@0,400;0,700;1,400;1,700&family=Playfair+Display:ital,wght@1,900&display=swap">
<style>
:root{
  --ink:#111112;
  --night:#1c1b1f;
  --bar:#232226;
  --black:#050505;
  --white:#ffffff;
  --paper:#ffffff;
  --grey:#9a9a9e;
  --line:#3a393d;
  --coral:#f0564f;
  --gold:#f2c14e;
  --sans:'Raleway', Arial, sans-serif;
  --serif:'Old Standard TT', Georgia, serif;
  --display:'Playfair Display', Georgia, serif;
}
*{box-sizing:border-box;margin:0;padding:0}
html,body{width:1200px;height:1000px;overflow:hidden;background:var(--paper)}
.canvas{position:relative;width:1200px;height:1000px;overflow:hidden;background:var(--paper);font-family:var(--sans);color:var(--ink)}
.abs{position:absolute}
.page-label{position:absolute;font-family:var(--serif);font-size:17px;letter-spacing:1px;color:var(--ink)}

/* shared pieces */
.social{position:absolute;display:flex}
.social span{display:flex;align-items:center;justify-content:center;border-left:1px solid var(--line)}
.social span:last-child{border-right:1px solid var(--line)}
.social span i{display:block;border-radius:50%;background:#d9d9dc}
.btn-outline{position:absolute;display:flex;align-items:center;justify-content:center;border:1px solid var(--gold);color:var(--white);text-transform:uppercase;letter-spacing:1px;font-weight:600}
.rule{position:absolute;height:1px;background:var(--coral)}
.hours{position:absolute;border:1.5px solid currentColor}
.hours h4{font-family:var(--serif);font-weight:400;text-align:center;letter-spacing:.5px}
.hours dl{display:grid;grid-template-columns:1fr auto}
.card-mark{position:absolute;display:flex;align-items:center;justify-content:center;background:#c9c9cc;color:#2a2a2e;font-weight:700;border-radius:2px}

/* ================= HOMEPAGE ================= */
.home{position:absolute;left:0;top:0;width:495px;height:1000px;background:var(--black);color:var(--white)}
.home .topbar{position:absolute;left:0;top:0;width:495px;height:13px;background:var(--bar);font-size:4px;color:#cfcfd2}
.home .topbar .info{position:absolute;top:4px}
.home .hero{position:absolute;left:0;top:13px;width:495px;height:270px;
  background:radial-gradient(ellipse 120px 150px at 245px 120px,#d98b6c 0%,#b5482a 35%,#5a2418 65%,transparent 100%),
             radial-gradient(ellipse 200px 180px at 250px 140px,#4a2a25 0%,#1c1718 70%),#141214}
.logo-home{position:absolute;left:77px;top:22px;width:85px}
.logo-home .name{font-family:var(--sans);font-weight:600;font-size:13px;letter-spacing:.5px;line-height:1}
.logo-home .sub{margin-top:2px;border-top:1px solid #fff;border-bottom:1px solid #fff;font-size:4px;letter-spacing:.8px;text-align:center;line-height:5px}
.nav-home{position:absolute;top:32px;left:238px;display:flex;gap:10px;font-size:4.5px;letter-spacing:.3px}
.book-home{position:absolute;left:378px;top:28px;width:40px;height:12px;background:#fff;color:#111;font-size:4.5px;font-weight:600;display:flex;align-items:center;justify-content:center}
.hero-word{position:absolute;left:80px;top:84px;font-family:var(--display);font-style:italic;font-weight:900;font-size:58px;line-height:1;color:#fff}
.hero-copy{position:absolute;left:82px;top:149px;font-weight:800;line-height:1}
.hero-copy .a{font-size:10px}
.hero-copy .b{font-size:19px;color:var(--gold)}
.hero-copy .c{font-size:9px}
.hero-cta{position:absolute;left:82px;top:194px;width:71px;height:12px;background:var(--coral);font-size:4px;letter-spacing:.8px;display:flex;align-items:center;justify-content:center;font-weight:600}
.hero-arrow{position:absolute;top:165px;width:12px;height:12px;border:1px solid #fff;border-radius:50%}
.dots{position:absolute;left:240px;top:272px;display:flex;gap:4px}
.dots i{width:3px;height:3px;border-radius:50%;background:#888}
.dots i:first-child{background:#fff}

.awarded{position:absolute;left:0;top:283px;width:495px;height:67px;background:var(--black);text-align:center}
.awarded h3{position:absolute;left:0;width:495px;top:15px;font-family:var(--serif);font-style:italic;font-weight:400;font-size:12px}
.awarded p{position:absolute;left:0;width:495px;top:40px;font-family:var(--serif);font-size:5.5px}

.antiage{position:absolute;left:0;top:350px;width:495px;height:156px;
  background:linear-gradient(90deg,#3a1c14 0%,#7a3522 22%,#5a3a30 38%,#2b2626 60%,#1e1d1e 100%)}
.antiage .copy{position:absolute;right:77px;top:37px;width:240px;height:84px;text-align:right}
.antiage .kick{position:absolute;right:0;top:0;font-size:4.5px;letter-spacing:.8px;white-space:nowrap}
.antiage h2{position:absolute;right:0;top:8px;font-family:var(--serif);font-weight:400;font-size:11.5px;letter-spacing:.6px;line-height:14px;white-space:nowrap}
.antiage p{position:absolute;right:0;top:33px;width:172px;font-size:4.3px;line-height:5.6px;color:#e4e4e6}

.promo-home{position:absolute;left:0;top:506px;width:495px;height:248px;background:var(--paper);color:var(--ink)}
.section-kick{position:absolute;text-align:center;font-family:var(--serif);letter-spacing:.8px}
.section-title{position:absolute;text-align:center;font-family:var(--serif);letter-spacing:1px}
.product-shot{position:absolute;background:radial-gradient(ellipse at 50% 55%,#2c2b30 0%,#0b0b0d 70%)}
.brand-title{position:absolute;font-weight:800;text-align:center}
.btn-dark{position:absolute;border:1px solid var(--ink);display:flex;align-items:center;justify-content:center;letter-spacing:1px;color:var(--ink)}

.tiles{position:absolute;left:0;top:754px;width:495px;height:108px;display:flex}
.tile{position:relative;width:124px;height:108px}
.tile:nth-child(1){background:linear-gradient(135deg,#2f2a2c,#6a5a55 60%,#3a3335)}
.tile:nth-child(2){background:linear-gradient(135deg,#3a2820,#8a5a42 55%,#4a3028)}
.tile:nth-child(3){background:linear-gradient(135deg,#444446,#8a8a8c 55%,#4e4e50)}
.tile:nth-child(4){background:linear-gradient(135deg,#2a2220,#6e4e40 55%,#33261f)}
.tile .t{position:absolute;left:25px;bottom:31px;font-family:var(--serif);font-style:italic;font-weight:700;font-size:9px;line-height:9px;color:#fff}
.tile .who{position:absolute;left:25px;top:77px;font-size:3.5px;color:var(--gold);letter-spacing:.4px}
.tile .btn{position:absolute;left:25px;top:84px;width:62px;height:12px;border:1px solid #fff;font-size:4px;letter-spacing:1px;display:flex;align-items:center;justify-content:center;color:#fff}

.foot-home{position:absolute;left:0;top:862px;width:495px;height:126px;background:var(--black)}
.foot-home h5{position:absolute;font-family:var(--serif);font-weight:400;font-size:6px;letter-spacing:.6px}
.foot-home ul{position:absolute;list-style:none;font-size:4px;line-height:11px}
.copy-home{position:absolute;left:0;top:988px;width:495px;height:12px;background:var(--bar);font-size:3.5px;color:#cfcfd2}

/* ================= BOOKING ================= */
.book{position:absolute;left:495px;top:77px;width:705px;height:923px;background:var(--paper)}
.book .topbar{position:absolute;left:0;top:0;width:705px;height:20px;background:var(--bar);color:#d5d5d8;font-size:5.5px}
.book .header{position:absolute;left:0;top:20px;width:705px;height:60px;background:var(--night);color:#fff}
.logo-book{position:absolute;left:109px;top:13px;width:119px}
.logo-book .name{font-family:var(--sans);font-weight:600;font-size:19px;letter-spacing:.6px;line-height:1}
.logo-book .sub{margin-top:3px;border-top:1px solid #fff;border-bottom:1px solid #fff;font-size:5.5px;letter-spacing:1.1px;text-align:center;line-height:7px}
.nav-book{position:absolute;top:26px;left:338px;display:flex;gap:18px;font-size:6px;letter-spacing:.3px}
.book-btn{position:absolute;left:537px;top:20px;width:58px;height:17px;background:#fff;color:#111;font-size:6px;font-weight:600;display:flex;align-items:center;justify-content:center}

.salon-shot{position:absolute;left:109px;top:110px;width:168px;height:110px;background:linear-gradient(180deg,#e8e8ea 0%,#bdbdc0 45%,#6c6c70 75%,#d0d0d2 100%)}
.book-title{position:absolute;left:286px;top:119px;font-family:var(--serif);font-style:italic;font-weight:400;font-size:13.5px;letter-spacing:.8px}
.book-intro{position:absolute;left:286px;top:150px;font-family:var(--serif);font-size:6.5px}
.field{position:absolute;height:12px;border-bottom:1.5px solid var(--ink);font-size:6.5px;color:#9a9a9e}
.deposit-label{position:absolute;left:290px;top:285px;font-size:7px}
.deposit-input{position:absolute;left:329px;top:279px;width:54px;height:20px;border:1px solid #777;font-size:6.5px;display:flex;align-items:center;justify-content:space-between;padding:0 5px}
.deposit-input .cur{color:#9a9a9e}
.checkout{position:absolute;left:329px;top:308px;width:84px;height:17px;background:var(--coral);color:#fff;font-size:6px;letter-spacing:1.2px;font-weight:600;display:flex;align-items:center;justify-content:center;gap:5px}
.divider{position:absolute;left:0;top:375px;width:705px;height:1px;background:#bdbdc0}

.foot-book{position:absolute;left:0;top:728px;width:705px;height:175px;background:var(--black);color:#fff}
.foot-book h5{position:absolute;font-family:var(--serif);font-weight:400;font-size:8px;letter-spacing:.8px}
.foot-book ul{position:absolute;list-style:none;font-size:5.5px;line-height:16px}
.copy-book{position:absolute;left:0;top:903px;width:705px;height:20px;background:var(--bar);font-size:5.5px;color:#d5d5d8}
</style>
</head>
<body>
<div class="canvas">

  <svg class="abs" style="left:520px;top:24px" width="58" height="16" viewBox="0 0 58 16" aria-hidden="true">
    <line x1="3" y1="8" x2="57" y2="8" stroke="#111" stroke-width="1.8"/>
    <path d="M10 1 L2 8 L10 15" fill="none" stroke="#111" stroke-width="1.8"/>
  </svg>
  <div class="page-label" style="left:586px;top:21px">HOMEPAGE</div>
  <div class="page-label" style="left:797px;top:15px">BOOKAPPOINTMENT STEP 1</div>
  <svg class="abs" style="left:882px;top:42px" width="14" height="24" viewBox="0 0 14 24" aria-hidden="true">
    <line x1="7" y1="0" x2="7" y2="22" stroke="#111" stroke-width="1.8"/>
    <path d="M1 15 L7 22 L13 15" fill="none" stroke="#111" stroke-width="1.8"/>
  </svg>

  <!-- ================= HOMEPAGE ================= -->
  <section class="home">
    <div class="hero" role="img" aria-label="Hero photo: smiling woman with curly red hair and bright makeup on a dark background"></div>

    <div class="topbar">
      <svg class="abs" style="left:77px;top:3px" width="4" height="7" viewBox="0 0 4 7" aria-hidden="true"><rect x=".4" y=".4" width="3.2" height="6.2" rx=".6" fill="none" stroke="#ccc" stroke-width=".6"/></svg>
      <span class="info" style="left:83px">Customer Support &amp; Sales 0800 555 0142</span>
      <svg class="abs" style="left:168px;top:3px" width="5" height="7" viewBox="0 0 5 7" aria-hidden="true"><path d="M2.5 6.6 C1 4.6 .4 3.6 .4 2.5 A2.1 2.1 0 0 1 4.6 2.5 C4.6 3.6 4 4.6 2.5 6.6Z" fill="#ccc"/></svg>
      <span class="info" style="left:175px">Unit 4B, Elm Business Park LS99 1ZZ</span>
      <div class="social" style="left:357px;top:0;height:13px">
        <span style="width:10.5px;height:13px"><i style="width:3px;height:3px"></i></span>
        <span style="width:10.5px;height:13px"><i style="width:3px;height:3px"></i></span>
        <span style="width:10.5px;height:13px"><i style="width:3px;height:3px"></i></span>
        <span style="width:10.5px;height:13px"><i style="width:3px;height:3px"></i></span>
        <span style="width:10.5px;height:13px"><i style="width:3px;height:3px"></i></span>
        <span style="width:10.5px;height:13px"><i style="width:3px;height:3px"></i></span>
      </div>
    </div>

    <div class="logo-home"><div class="name">GLOWHOUSE</div><div class="sub">BEAUTY &amp; MAKEUP CENTER</div></div>
    <nav class="nav-home"><span>HOME</span><span>PAGES</span><span>ABOUT US</span><span>GALLERY</span><span>BLOG</span></nav>
    <div class="book-home">BOOK ONLINE</div>

    <div class="hero-word">Makeup</div>
    <div class="hero-copy"><div class="a">FIND OUT OUR</div><div class="b">SERVICES</div><div class="c">&amp; DISCOUNTS</div></div>
    <div class="hero-cta">DISCOVER MORE</div>
    <div class="btn-outline" style="left:335px;top:176px;width:62px;height:21px;font-size:4px;line-height:5px;text-align:center">CHECK OUT OUR<br>HOT NEWS</div>
    <div class="btn-outline" style="left:364px;top:214px;width:58px;height:13px;font-size:4px">OPENING TIMINGS</div>
    <div class="hero-arrow" style="left:28px"><svg width="10" height="10" viewBox="0 0 10 10" aria-hidden="true"><path d="M6 2.5 L3.5 5 L6 7.5" fill="none" stroke="#fff" stroke-width="1"/></svg></div>
    <div class="hero-arrow" style="left:456px"><svg width="10" height="10" viewBox="0 0 10 10" aria-hidden="true"><path d="M4 2.5 L6.5 5 L4 7.5" fill="none" stroke="#fff" stroke-width="1"/></svg></div>
    <div class="dots"><i></i><i></i><i></i></div>

    <div class="awarded">
      <h3>Awarded</h3>
      <div class="rule" style="left:240px;top:32px;width:15px"></div>
      <p>One of the Best Hair Salons in the City</p>
    </div>

    <section class="antiage" role="img" aria-label="Photo: portrait of a woman with red hair showing an anti-age makeup look">
      <div class="copy">
        <div class="kick">WE WANT YOU TO LOOK FABULOUS</div>
        <h2>ANTI-AGE MAKEUP STYLE</h2>
        <div class="rule" style="right:0;top:27px;width:13px"></div>
        <p>Our anti-age looks use light, hydrating layers that soften fine lines and bring back a natural glow. Each session starts with careful skin prep and a short chat about your routine, so the finish suits your face, your day and your plans for the evening. We choose textures that stay fresh for hours and never settle into creases.</p>
        <div class="btn-outline" style="right:0;top:69px;width:47px;height:12px;font-size:4px">READ MORE</div>
      </div>
    </section>

    <section class="promo-home">
      <div class="section-kick" style="left:0;width:495px;top:20px;font-size:5px">BEWARE OF CURRENT PROMOTIONS</div>
      <div class="section-title" style="left:0;width:495px;top:29px;font-size:12.5px">WORTH TO LOOK</div>
      <div class="rule" style="left:240px;top:45px;width:15px"></div>
      <div class="product-shot" style="left:77px;top:67px;width:176px;height:154px" role="img" aria-label="Product photo: black jar of cream eyeliner"></div>
      <div class="brand-title" style="left:262px;width:145px;top:129px;font-size:12px">VELVET CANVAS</div>
      <div class="btn-dark" style="left:297px;top:146px;width:76px;height:12px;font-size:4.5px">SEE PROMOTIONS</div>
    </section>

    <div class="tiles">
      <div class="tile" role="img" aria-label="Photo: close-up of a woman with dark hair and hydrated skin">
        <div class="t">I WANT<br>HYDRATION<br>AND LIGHT</div><div class="who">MAYA // LONDON</div><div class="btn">VIEW MORE</div>
      </div>
      <div class="tile" role="img" aria-label="Photo: woman with bold styled makeup">
        <div class="t">I WANT STYLE</div><div class="who">SPECIAL GUEST</div><div class="btn">VIEW MORE</div>
      </div>
      <div class="tile" role="img" aria-label="Photo: woman with light, relaxed makeup">
        <div class="t">I WANT LIGHT<br>AND LIESURE</div><div class="who">IRIS // LONDON</div><div class="btn">VIEW MORE</div>
      </div>
      <div class="tile" role="img" aria-label="Photo: woman with voluminous natural hair">
        <div class="t">I WANT<br>VOLUME AND<br>NATURALNESS</div><div class="who">NORA // NYC</div><div class="btn">VIEW MORE</div>
      </div>
    </div>

    <footer class="foot-home">
      <h5 style="left:77px;top:20px">NEWSLETTER</h5>
      <div class="abs" style="left:77px;top:39px;width:61px;height:11px;border:1px solid #fff;font-size:3.8px;padding:3px 4px">EMAIL ADDRESS</div>
      <div class="btn-outline" style="left:77px;top:53px;width:31px;height:12px;font-size:3.8px;letter-spacing:.3px;color:var(--gold)">SUBSCRIBE</div>
      <h5 style="left:77px;top:77px">WE ACCEPT</h5>
      <div class="card-mark" style="left:77px;top:89px;width:20px;height:12px;font-size:3.5px">NOVA</div>
      <div class="card-mark" style="left:100px;top:89px;width:20px;height:12px;font-size:3px">PAYLINE</div>
      <h5 style="left:166px;top:20px">ABOUT US</h5>
      <ul style="left:166px;top:34px"><li>About us</li><li>Gift Cards</li><li>Terms &amp; Conditions</li><li>Work With Us</li></ul>
      <h5 style="left:254px;top:20px">CUSTOMER CARE</h5>
      <ul style="left:254px;top:34px"><li>Contact us</li><li>Delivery Information</li><li>Returns Policy</li><li>Privacy and Security</li></ul>
      <div class="hours" style="left:344px;top:21px;width:75px;height:78px;padding:8px 9px;color:#fff">
        <h4 style="font-size:5px">OPENING TIMING</h4>
        <dl style="margin-top:7px;font-size:3.8px;line-height:7.4px">
          <dt>Monday</dt><dd>08:00 – 17:30</dd><dt>Tuesday</dt><dd>08:00 – 17:30</dd><dt>Wednesday</dt><dd>08:00 – 17:30</dd><dt>Thursday</dt><dd>08:00 – 17:30</dd><dt>Friday</dt><dd>08:00 – 17:30</dd><dt>Saturday</dt><dd>12:00 – 17:30</dd><dt>Sunday</dt><dd>CLOSED</dd>
        </dl>
      </div>
    </footer>
    <div class="copy-home">
      <span class="abs" style="left:77px;top:4px">© 2010 – 2014 www.glowhouse-salon.com. All rights reserved.</span>
      <div class="social" style="left:357px;top:0;height:12px">
        <span style="width:10.5px;height:12px"><i style="width:3px;height:3px"></i></span>
        <span style="width:10.5px;height:12px"><i style="width:3px;height:3px"></i></span>
        <span style="width:10.5px;height:12px"><i style="width:3px;height:3px"></i></span>
        <span style="width:10.5px;height:12px"><i style="width:3px;height:3px"></i></span>
        <span style="width:10.5px;height:12px"><i style="width:3px;height:3px"></i></span>
        <span style="width:10.5px;height:12px"><i style="width:3px;height:3px"></i></span>
      </div>
    </div>
  </section>

  <!-- ================= BOOKING STEP 1 ================= -->
  <section class="book">
    <div class="topbar">
      <svg class="abs" style="left:109px;top:5px" width="6" height="10" viewBox="0 0 6 10" aria-hidden="true"><rect x=".5" y=".5" width="5" height="9" rx="1" fill="none" stroke="#ddd" stroke-width=".8"/></svg>
      <span class="abs" style="left:118px;top:7px">Customer Support &amp; Sales 0800 555 0142</span>
      <svg class="abs" style="left:237px;top:5px" width="6" height="10" viewBox="0 0 6 10" aria-hidden="true"><path d="M3 9.5 C1.2 6.8 .5 5.3 .5 3.5 A2.5 2.5 0 0 1 5.5 3.5 C5.5 5.3 4.8 6.8 3 9.5Z" fill="#ddd"/></svg>
      <span class="abs" style="left:247px;top:7px">Unit 4B, Elm Business Park LS99 1ZZ</span>
      <div class="social" style="left:507px;top:0;height:20px">
        <span style="width:18px;height:20px"><i style="width:4px;height:4px"></i></span>
        <span style="width:18px;height:20px"><i style="width:4px;height:4px"></i></span>
        <span style="width:18px;height:20px"><i style="width:4px;height:4px"></i></span>
        <span style="width:18px;height:20px"><i style="width:4px;height:4px"></i></span>
        <span style="width:18px;height:20px"><i style="width:4px;height:4px"></i></span>
      </div>
    </div>

    <header class="header">
      <div class="logo-book"><div class="name">GLOWHOUSE</div><div class="sub">BEAUTY &amp; MAKEUP CENTER</div></div>
      <nav class="nav-book"><span>HOME</span><span>PAGES</span><span>ABOUT US</span><span>GALLERY</span><span>BLOG</span></nav>
      <div class="book-btn">BOOK ONLINE</div>
    </header>

    <div class="salon-shot" role="img" aria-label="Photo: bright salon interior with styling chairs and mirrors"></div>
    <div class="hours" style="left:109px;top:233px;width:124px;height:106px;padding:11px 0 0;color:var(--ink)">
      <h4 style="font-size:7.5px">OPENING TIMING</h4>
      <dl style="margin:12px 0 0 21px;width:82px;font-size:5.5px;line-height:8.8px">
        <dt>Monday</dt><dd>08:00 – 17:30</dd><dt>Tuesday</dt><dd>08:00 – 17:30</dd><dt>Wednesday</dt><dd>08:00 – 17:30</dd><dt>Thrusday</dt><dd>08:00 – 17:30</dd><dt>Friday</dt><dd>08:00 – 17:30</dd><dt>Saturday</dt><dd>12:00 – 17:30</dd><dt>Sunday</dt><dd>CLOSED</dd>
      </dl>
    </div>

    <h1 class="book-title">BOOK AN APPOINTMENT NOW</h1>
    <div class="rule" style="left:286px;top:140px;width:22px"></div>
    <p class="book-intro">Book your makeup, hairstyling or beauty appointment.</p>
    <div class="field" style="left:286px;top:174px;width:141px;height:16px">Name (Required)</div>
    <div class="field" style="left:453px;top:174px;width:141px;height:16px">Email (Required)</div>
    <div class="field" style="left:286px;top:200px;width:141px;height:16px">Telephone &nbsp;(Optional)</div>
    <div class="field" style="left:453px;top:200px;width:141px;height:16px">Appointment Time (Required)</div>
    <div class="field" style="left:286px;top:227px;width:308px;height:42px">Your Message</div>
    <div class="deposit-label">Deposit</div>
    <div class="deposit-input"><span>0.00</span><span class="cur">USD</span></div>
    <div class="checkout">CHECKOUT
      <svg width="12" height="6" viewBox="0 0 12 6" aria-hidden="true"><line x1="0" y1="3" x2="11" y2="3" stroke="#fff" stroke-width="1"/><path d="M8 .5 L11 3 L8 5.5" fill="none" stroke="#fff" stroke-width="1"/></svg>
    </div>

    <div class="divider"></div>

    <div class="section-kick" style="left:0;width:705px;top:404px;font-size:7px">BEWARE OF CURRENT PROMOTIONS</div>
    <div class="section-title" style="left:0;width:705px;top:416px;font-size:17px">WORTH TO LOOK</div>
    <div class="rule" style="left:341px;top:441px;width:22px"></div>
    <div class="product-shot" style="left:109px;top:470px;width:251px;height:221px;border:1px solid #222" role="img" aria-label="Product photo: gold colour cream tube standing on a black background"></div>
    <div class="brand-title" style="left:380px;width:192px;top:558px;font-size:18px">VELVET CANVAS</div>
    <div class="btn-dark" style="left:422px;top:583px;width:109px;height:17px;font-size:6px;border-width:1.5px">SEE PROMOTIONS</div>

    <footer class="foot-book">
      <h5 style="left:109px;top:28px">NEWSLETTER</h5>
      <div class="abs" style="left:109px;top:53px;width:88px;height:18px;border:1px solid #fff;font-size:5.5px;padding:5px 5px">EMAIL ADDRESS</div>
      <div class="btn-outline" style="left:109px;top:75px;width:44px;height:17px;font-size:5.5px;letter-spacing:.4px;color:var(--gold)">SUBSCRIBE</div>
      <h5 style="left:109px;top:108px">WE ACCEPT</h5>
      <div class="card-mark" style="left:109px;top:125px;width:29px;height:17px;font-size:5.5px">NOVA</div>
      <div class="card-mark" style="left:142px;top:125px;width:29px;height:17px;font-size:4.5px">PAYLINE</div>
      <h5 style="left:236px;top:28px">ABOUT US</h5>
      <ul style="left:236px;top:47px"><li>About us</li><li>Gift Cards</li><li>Terms &amp; Conditions</li><li>Work With Us</li></ul>
      <h5 style="left:361px;top:28px">CUSTOMER CARE</h5>
      <ul style="left:361px;top:47px"><li>Contact us</li><li>Delivery Information</li><li>Returns Policy</li><li>Privacy and Security</li></ul>
      <div class="hours" style="left:490px;top:30px;width:106px;height:106px;padding:11px 0 0;color:#fff">
        <h4 style="font-size:7.5px">OPENING TIMING</h4>
        <dl style="margin:10px 0 0 13px;width:80px;font-size:5.5px;line-height:8.8px">
          <dt>Monday</dt><dd>08:00 – 17:30</dd><dt>Tuesday</dt><dd>08:00 – 17:30</dd><dt>Wednesday</dt><dd>08:00 – 17:30</dd><dt>Thursday</dt><dd>08:00 – 17:30</dd><dt>Friday</dt><dd>08:00 – 17:30</dd><dt>Saturday</dt><dd>12:00 – 17:30</dd><dt>Sunday</dt><dd>CLOSED</dd>
        </dl>
      </div>
    </footer>
    <div class="copy-book">
      <span class="abs" style="left:109px;top:7px">© 2010 – 2014 www.glowhouse-salon.com. All rights reserved.</span>
      <div class="social" style="left:507px;top:0;height:20px">
        <span style="width:18px;height:20px"><i style="width:4px;height:4px"></i></span>
        <span style="width:18px;height:20px"><i style="width:4px;height:4px"></i></span>
        <span style="width:18px;height:20px"><i style="width:4px;height:4px"></i></span>
        <span style="width:18px;height:20px"><i style="width:4px;height:4px"></i></span>
        <span style="width:18px;height:20px"><i style="width:4px;height:4px"></i></span>
      </div>
    </div>
  </section>

</div>
</body>
</html>
```